Ridgefern Hollow Post Card advertising my new real estate website

I want to send a postcard to owners in the community of Ridgefern Hollow Advertising my new website. www.ridgefernhollowsearch.com This is a page on www.ednacarverrealty.com I would like to use the home page picture on www.ridgefernhollowsearch.com as the main big picture and keep the search field on it. on the front of the postcard with my contact info and logo along the bottom of the postcard. On the back of the card I would like to have one side address what is available on the website and include the "how much is your home worth" widget on my webdite along with the Items and I like the check marks for Interactive Map Search, Free Daily Email Updates, Automated Home Searches, Favorite Properties, And Much More. You should be able to find all my logos and contact information on my website or attached below

Target Market(s)

Lot and Homeowners in the community of Ridgefern Hollow

Industry/Entity Type

Real Estate Agent

Font styles to use
Serif

Colors
0255a3
0592cd
fbed22

Requirements
Must have
• I am a real estate agent - I don't want the front to be too busy just the main page picture and my logos and contact information at the bottom. Also highlighting the www.ridgefernhollowsearch.com web address prominent on big picture
• use the www.ednacarverrealty.com web address with contact info at bottom
Nice to have
• This will be mailed so one side of the back of the card should have what I mentioned above regrading home worth widget and check marked features and the other side should be left for mailing purposes. Name logo and return address should be there and for this portion only use the Thornwick Mallory or TM logo as the name of my company and return address will be to Thornwick Mallory Realty

```html
<!DOCTYPE html>
<html lang="en">
<head>
<meta charset="utf-8">
<title>Ridgefern Hollow Real Estate Search Postcard</title>
<link rel="stylesheet" href="https://fonts.googleapis.com/css2?family=Cinzel:wght@700;800&family=Oswald:wght@500;600&family=Roboto+Condensed:wght@400;500&family=Mulish:wght@400;600;700&display=swap">
<style>
:root{
  --navy:#0255a3;
  --sky:#0592cd;
  --yellow:#fbed22;
  --ink:#1b1b1b;
  --ink-blue:#1d3f8c;
  --pale-blue:#cfe7f4;
  --panel-band:#e6e6e6;
  --stage:#ececec;
  --green:#3cc51a;
}
*{box-sizing:border-box;margin:0;padding:0}
html,body{width:982px;height:1200px;overflow:hidden;background:var(--stage)}
.stage{position:absolute;left:0;top:0;width:900px;height:1100px;transform:scale(1.0911);transform-origin:0 0;font-family:'Mulish',sans-serif;color:var(--ink)}
.card{position:absolute;left:67px;width:766px;height:492px;background:#fff;overflow:hidden;box-shadow:0 3px 10px rgba(0,0,0,.18)}
.card--front{top:38px}
.card--back{top:577px;height:493px}

/* front */
.hero-photo{position:absolute;left:0;top:0;width:766px;height:412px;
  background:linear-gradient(180deg,#3f7fd0 0%,#7fb2e3 22%,#a9c9de 30%,#5d8fae 36%,#6c8a8a 50%,#7c8f78 62%,#5d7a4e 78%,#4f6a3b 100%)}
.hero-title{position:absolute;left:0;top:34px;width:766px;text-align:center;font-family:'Cinzel',serif;font-weight:700;font-size:31px;color:#fff;letter-spacing:.5px;text-shadow:0 2px 4px rgba(0,0,0,.45)}
.hero-url{position:absolute;left:383px;top:95px;font-family:'Oswald',sans-serif;font-weight:600;font-size:25px;color:var(--yellow);letter-spacing:.2px;text-shadow:0 2px 3px rgba(0,0,0,.5)}
.search-panel{position:absolute;left:50px;top:89px;width:286px;height:253px;border-radius:6px;background:rgba(255,255,255,.55);border:1px solid rgba(255,255,255,.7);font-size:10.5px;color:#222}
.field-label{position:absolute;font-size:10.5px}
.select{position:absolute;height:18px;background:#fff;border:1px solid #bbb;font-size:9.5px;line-height:16px;padding-left:10px}
.select::after{content:"";position:absolute;right:0;top:0;width:16px;height:16px;border-left:1px solid #ccc;background:linear-gradient(#eee,#ddd)}
.select .caret{position:absolute;right:5px;top:6px;width:0;height:0;border-left:3.5px solid transparent;border-right:3.5px solid transparent;border-top:4px solid #555;z-index:1}
.to-label{position:absolute;left:136px;top:81px;font-size:10.5px}
.checks{position:absolute;left:23px;top:164px;display:flex;gap:9px;font-size:8.5px}
.checks span{display:flex;align-items:center;gap:3px}
.checks i{display:inline-block;width:8px;height:8px;border:1px solid #888;background:#fff;font-style:normal;font-size:8px;line-height:6px;text-align:center}
.search-btn{position:absolute;left:22px;top:200px;width:107px;height:31px;border-radius:3px;background:linear-gradient(#3a55b8,#1a2d8a);border:1px solid #132070;color:#fff;font-size:14px;text-align:center;line-height:29px}
.adv-link{position:absolute;left:156px;top:208px;font-size:12.5px;color:var(--navy);text-decoration:underline}
.front-band{position:absolute;left:0;top:0;width:766px;height:492px}
.name-tag{position:absolute;left:533px;top:369px;width:212px;height:27px;background:var(--sky);color:#fff;font-family:'Roboto Condensed',sans-serif;font-weight:500;font-size:13.5px;line-height:27px;text-align:center}
.contact{position:absolute;font-family:'Mulish',sans-serif;color:var(--ink-blue);text-align:right}
.contact p{display:flex;justify-content:flex-end;align-items:center;gap:5px;white-space:nowrap}
.contact svg{flex:none}
.contact .phone{font-weight:700}
.front-contact{right:31px;top:402px;font-size:11.5px;line-height:17px}
.logo-row{position:absolute;display:flex;align-items:center}
.brand-mark{display:flex;align-items:center;gap:5px;font-family:'Mulish',sans-serif;font-weight:700;color:var(--ink);white-space:nowrap}
.brand-mark b{display:inline-block;background:var(--ink);border-radius:50%}
.divider{width:1px;background:#cfcfcf;align-self:stretch}
.brand-assoc{color:var(--navy)}
.brand-assoc b{background:#e58a2c;border-radius:2px}

/* back */
.back-copy{position:absolute;left:0;top:0;width:470px;height:431px;background:linear-gradient(180deg,#fff 0%,#f3f3f3 60%,#fff 100%)}
.chevron{position:absolute;left:0;top:0}
.headline{position:absolute;left:28px;top:20px;font-family:'Cinzel',serif;font-weight:700;color:var(--sky);font-size:27px;line-height:33px;letter-spacing:.5px}
.headline strong{color:var(--navy);font-weight:800}
.subline{position:absolute;left:26px;top:88px;font-size:22px;color:var(--navy);letter-spacing:.2px}
.value-form{position:absolute;left:27px;top:127px;width:361px;height:38px;display:flex;border:1px solid #cfcfcf;background:#e9e9e9}
.value-form .addr{flex:1;font-size:10px;color:#9a9a9a;line-height:36px;padding-left:12px;border-right:1px solid #cfcfcf}
.value-form .unit{width:62px;font-size:15px;color:#9a9a9a;line-height:36px;padding-left:10px}
.value-form .submit{width:79px;background:var(--green);color:#fff;font-size:18px;line-height:36px;text-align:center}
.features{position:absolute;left:33px;top:181px;list-style:none;font-family:'Roboto Condensed',sans-serif;font-size:13.5px;color:var(--navy)}
.features li{display:flex;align-items:center;gap:7px;height:21.5px}
.back-name{position:absolute;right:377px;top:183px;font-family:'Roboto Condensed',sans-serif;font-weight:500;font-size:12px;color:var(--ink)}
.back-contact{right:377px;top:205px;font-size:11px;line-height:15.5px}
.social{position:absolute;left:300px;top:311px;display:flex;gap:9px}
.social span{width:22px;height:22px;border-radius:50%;background:var(--sky)}
.back-band{position:absolute;left:0;top:431px;width:766px;height:62px;background:var(--panel-band)}
.stamp{position:absolute;left:674px;top:28px;width:65px;height:73px;border:1px solid #333}
.mail-line{position:absolute;left:526px;width:212px;height:1px;background:#888}
</style>
</head>
<body>
<div class="stage">

  <section class="card card--front">
    <div class="hero-photo" role="img" aria-label="Aerial photograph of the Ridgefern Hollow canal community with coastline and sky"></div>
    <h1 class="hero-title">Ridgefern Hollow Real Estate Search</h1>
    <div class="hero-url">www.ridgefernhollowsearch.com</div>

    <div class="search-panel">
      <span class="field-label" style="left:22px;top:17px">City</span>
      <div class="select" style="left:22px;top:32px;width:106px">Fernport<span class="caret"></span></div>
      <span class="field-label" style="left:155px;top:17px">Subdivision</span>
      <div class="select" style="left:155px;top:32px;width:106px">All Subdivisions<span class="caret"></span></div>
      <span class="field-label" style="left:22px;top:57px">Price</span>
      <div class="select" style="left:22px;top:72px;width:96px">No Limit<span class="caret"></span></div>
      <span class="to-label">TO</span>
      <div class="select" style="left:165px;top:72px;width:96px">No Limit<span class="caret"></span></div>
      <span class="field-label" style="left:22px;top:102px">Beds</span>
      <div class="select" style="left:22px;top:116px;width:52px">Any<span class="caret"></span></div>
      <span class="field-label" style="left:120px;top:102px">Baths</span>
      <div class="select" style="left:120px;top:116px;width:52px">Any<span class="caret"></span></div>
      <span class="field-label" style="left:22px;top:147px">Property Type</span>
      <div class="checks">
        <span><i>&#10003;</i>Home</span>
        <span><i>&#10003;</i>Condo</span>
        <span><i></i>Land</span>
        <span style="margin-left:8px"><i></i>Multi-Res</span>
      </div>
      <div class="search-btn">Search</div>
      <div class="adv-link">Advanced Search</div>
    </div>

    <svg class="front-band" width="766" height="492" viewBox="0 0 766 492" aria-hidden="true">
      <polygon points="0,412 766,412 766,492 0,492" fill="#fff"/>
      <polygon points="490,388 766,370 766,492 445,492" fill="var(--pale-blue)"/>
      <polygon points="490,388 766,370 766,376 495,394 451,492 445,492" fill="var(--navy)"/>
      <polygon points="490,388 532,385 514,412 477,412" fill="#d3c23a" opacity=".9"/>
    </svg>
    <div class="name-tag">Edna CarverThornwick Mallory Realty</div>
    <div class="contact front-contact">
      <p><svg width="9" height="12" viewBox="0 0 9 12"><path d="M4.5 0A4.5 4.5 0 0 0 0 4.5C0 8 4.5 12 4.5 12S9 8 9 4.5A4.5 4.5 0 0 0 4.5 0Zm0 6.2a1.7 1.7 0 1 1 0-3.4 1.7 1.7 0 0 1 0 3.4Z" fill="var(--sky)"/></svg>218 Linden Ave. PO Box 312</p>
      <p>Fernport, FL 30417</p>
      <p class="phone" style="font-size:12.5px"><svg width="12" height="12" viewBox="0 0 12 12"><circle cx="6" cy="6" r="5.3" fill="none" stroke="var(--sky)" stroke-width="1.2"/><path d="M4 3.2l1 1.3-.6.8a4 4 0 0 0 2.3 2.3l.8-.6 1.3 1-.6 1C6.3 9 3 5.7 3 3.8Z" fill="var(--sky)"/></svg>(555) 218-0473</p>
      <p><svg width="12" height="9" viewBox="0 0 12 9"><rect x=".6" y=".6" width="10.8" height="7.8" fill="none" stroke="var(--sky)" stroke-width="1.1"/><path d="M.6.6 6 5l5.4-4.4" fill="none" stroke="var(--sky)" stroke-width="1.1"/></svg>ednacarver@ednacarverrealty.com</p>
      <p><svg width="10" height="10" viewBox="0 0 10 10"><circle cx="5" cy="5" r="4.4" fill="none" stroke="var(--sky)" stroke-width="1"/><path d="M.6 5h8.8M5 .6c-2.4 2.6-2.4 6.2 0 8.8M5 .6c2.4 2.6 2.4 6.2 0 8.8" fill="none" stroke="var(--sky)" stroke-width=".8"/></svg>www.ednacarverrealty.com</p>
    </div>
    <div class="logo-row" style="left:30px;top:425px;height:50px;gap:10px">
      <div class="brand-mark" style="font-size:11px"><b style="width:12px;height:12px"></b>thornwick-mallory realty</div>
      <div class="divider"></div>
      <div class="brand-mark" style="font-size:11px">Harbor Circle Estates</div>
      <div class="divider"></div>
      <div class="brand-mark brand-assoc" style="font-size:11px"><b style="width:10px;height:10px"></b>EDNA CARVER</div>
    </div>
  </section>

  <section class="card card--back">
    <div class="back-copy"></div>
    <svg class="chevron" width="766" height="431" viewBox="0 0 766 431" aria-hidden="true">
      <polygon points="395,0 410,0 470,105 400,431 388,431 455,105" fill="var(--sky)"/>
    </svg>
    <h2 class="headline">How much is<br>your home <strong>worth?</strong></h2>
    <p class="subline">...get instant property value now!</p>
    <div class="value-form">
      <span class="addr">e.g. 1234 Your Street, Fernport, FL 30417</span>
      <span class="unit">Unit #</span>
      <span class="submit">Submit</span>
    </div>
    <ul class="features">
      <li><svg width="13" height="13" viewBox="0 0 13 13"><rect x=".5" y=".5" width="12" height="12" fill="#fff" stroke="#999"/><path d="M2.5 6.5l3 3 5-7" fill="none" stroke="var(--navy)" stroke-width="2"/></svg>Interactive Map Search,</li>
      <li><svg width="13" height="13" viewBox="0 0 13 13"><rect x=".5" y=".5" width="12" height="12" fill="#fff" stroke="#999"/><path d="M2.5 6.5l3 3 5-7" fill="none" stroke="var(--navy)" stroke-width="2"/></svg>Free Daily Email Updates,</li>
      <li><svg width="13" height="13" viewBox="0 0 13 13"><rect x=".5" y=".5" width="12" height="12" fill="#fff" stroke="#999"/><path d="M2.5 6.5l3 3 5-7" fill="none" stroke="var(--navy)" stroke-width="2"/></svg>Automated Home Searches,</li>
      <li><svg width="13" height="13" viewBox="0 0 13 13"><rect x=".5" y=".5" width="12" height="12" fill="#fff" stroke="#999"/><path d="M2.5 6.5l3 3 5-7" fill="none" stroke="var(--navy)" stroke-width="2"/></svg>Favorite Properties,</li>
      <li><svg width="13" height="13" viewBox="0 0 13 13"><rect x=".5" y=".5" width="12" height="12" fill="#fff" stroke="#999"/><path d="M2.5 6.5l3 3 5-7" fill="none" stroke="var(--navy)" stroke-width="2"/></svg>And Much More.</li>
    </ul>
    <div class="back-name">Edna CarverThornwick Mallory Realty</div>
    <div class="contact back-contact">
      <p><svg width="9" height="12" viewBox="0 0 9 12"><path d="M4.5 0A4.5 4.5 0 0 0 0 4.5C0 8 4.5 12 4.5 12S9 8 9 4.5A4.5 4.5 0 0 0 4.5 0Zm0 6.2a1.7 1.7 0 1 1 0-3.4 1.7 1.7 0 0 1 0 3.4Z" fill="var(--sky)"/></svg>218 Linden Ave. PO Box 312</p>
      <p>Fernport, FL 30417</p>
      <p class="phone" style="font-size:12px"><svg width="12" height="12" viewBox="0 0 12 12"><circle cx="6" cy="6" r="5.3" fill="none" stroke="var(--sky)" stroke-width="1.2"/><path d="M4 3.2l1 1.3-.6.8a4 4 0 0 0 2.3 2.3l.8-.6 1.3 1-.6 1C6.3 9 3 5.7 3 3.8Z" fill="var(--sky)"/></svg>(555) 218-0473</p>
      <p><svg width="12" height="9" viewBox="0 0 12 9"><rect x=".6" y=".6" width="10.8" height="7.8" fill="none" stroke="var(--sky)" stroke-width="1.1"/><path d="M.6.6 6 5l5.4-4.4" fill="none" stroke="var(--sky)" stroke-width="1.1"/></svg>ednacarver@ednacarverrealty.com</p>
      <p><svg width="10" height="10" viewBox="0 0 10 10"><circle cx="5" cy="5" r="4.4" fill="none" stroke="var(--sky)" stroke-width="1"/><path d="M.6 5h8.8M5 .6c-2.4 2.6-2.4 6.2 0 8.8M5 .6c2.4 2.6 2.4 6.2 0 8.8" fill="none" stroke="var(--sky)" stroke-width=".8"/></svg>www.ednacarverrealty.com</p>
    </div>
    <div class="social" aria-hidden="true"><span></span><span></span><span></span></div>
    <div class="logo-row" style="left:37px;top:308px;height:44px">
      <div class="brand-mark" style="font-size:15px"><b style="width:18px;height:18px"></b>thornwick-mallory realty</div>
    </div>
    <div class="logo-row" style="left:37px;top:368px;height:48px;gap:14px">
      <div class="brand-mark" style="font-size:14px">Harbor Circle Estates</div>
      <div class="divider"></div>
      <div class="brand-mark brand-assoc" style="font-size:14px"><b style="width:12px;height:12px"></b>EDNA CARVER</div>
    </div>
    <div class="back-band"></div>
    <div class="stamp"></div>
    <div class="mail-line" style="top:244px"></div>
    <div class="mail-line" style="top:277px"></div>
    <div class="mail-line" style="top:309px"></div>
  </section>

</div>
</body>
</html>
```